Sira Delcourt

Please look at the present Web Site – www.siradelcourt-example.co.za

Looking for a new modern slick design . The logo stays the same as well as font. The colors are same but can be toned down a little.
Examples of sites which are liked.
Vortyxgrey-example.com.au
corafleur-example.co.za

Please not I only require PSD files not coding.

Adults 25 up all groups

• Flash banner on home page?

```html
<!DOCTYPE html>
<html lang="en">
<head>
<meta charset="utf-8">
<title>Sira Delcourt – Sensuality Boutique</title>
<link rel="stylesheet" href="https://fonts.googleapis.com/css2?family=Montserrat:ital,wght@0,300;0,400;0,600;0,700;0,800;1,600&display=swap">
<style>
  :root {
    --bg: #050006;
    --bg-deep: #1a0420;
    --purple: #8a2bc4;
    --purple-bright: #a23fde;
    --purple-dark: #3a0b4e;
    --lilac: #b9a0d8;
    --lilac-soft: #a486c4;
    --text-muted: #b99bcf;
    --white: #f4eefa;
    --accent: #b23ce8;
    --line: #2c1736;
  }
  * { box-sizing: border-box; margin: 0; padding: 0; }
  html, body { width: 1200px; height: 837px; overflow: hidden; background: var(--bg); }
  .page {
    position: relative; width: 1200px; height: 837px; overflow: hidden;
    background: radial-gradient(ellipse 900px 500px at 600px 330px, var(--bg-deep) 0%, #0c0210 55%, var(--bg) 100%);
    font-family: Arial, Helvetica, sans-serif;
  }

  .top-nav {
    position: absolute; left: 0; top: 14px; width: 1200px; height: 35px;
    background: linear-gradient(#3a1550, #25093a 60%, #1c0629);
    border-bottom: 1px solid #4a1d63;
    font-size: 11.5px; color: var(--lilac-soft);
    display: flex; align-items: center; padding-left: 163px; white-space: nowrap;
  }
  .top-nav .sep { margin: 0 3px; }
  .top-nav .account { margin-left: 14px; }

  .brand {
    position: absolute; left: 319px; top: 52px; width: 545px; height: 155px;
    background: radial-gradient(ellipse 300px 90px at 50% 50%, #3a2a40 0%, #1b1020 60%, rgba(10,2,14,0) 100%);
  }
  .brand-name {
    position: absolute; left: 0; top: 46px; width: 545px; text-align: center;
    font-family: Montserrat, sans-serif; font-weight: 400; font-size: 50px; color: var(--white); letter-spacing: 1px;
  }
  .brand-tagline {
    position: absolute; left: 0; top: 112px; width: 545px; text-align: center;
    font-family: Montserrat, sans-serif; font-weight: 400; font-size: 15px; color: var(--white);
  }

  .categories {
    position: absolute; left: 133px; top: 222px; width: 332px; height: 317px;
    background: linear-gradient(90deg, #12041a, #240a30 30%, #1e0828 70%, #10031a);
    border: 1px solid #3a2046;
  }
  .categories-head {
    height: 48px; background: linear-gradient(#a43ee0, #7a22b4);
    border-bottom: 2px solid #c06bf0;
    font-family: Montserrat, sans-serif; font-weight: 800; font-size: 22px; color: var(--white);
    padding: 12px 0 0 31px; letter-spacing: .5px;
  }
  .categories ul { list-style: none; padding-top: 26px; }
  .categories li {
    height: 37.5px; font-family: Montserrat, sans-serif; font-weight: 600; font-size: 13px;
    color: var(--white); padding-left: 33px; position: relative;
  }
  .categories li.active::before {
    content: ""; position: absolute; left: 20px; top: -7px; width: 173px; height: 27px; border-radius: 10px;
    background: linear-gradient(#a446e2, #6a1a9c); z-index: 0;
  }
  .categories li span { position: relative; z-index: 1; }
  .categories-foot {
    position: absolute; left: 0; bottom: 8px; width: 100%; height: 2px; background: #4a3a52;
  }

  .welcome {
    position: absolute; left: 500px; top: 222px; width: 564px; height: 319px;
    background: #07020a; border: 1px solid #2b1a33; padding: 5px 6px;
  }
  .welcome-inner {
    width: 100%; height: 100%;
    background: radial-gradient(ellipse 320px 200px at 50% 40%, #4a1a68 0%, #2c0b40 60%, #1c0628 100%);
    text-align: center; padding-top: 46px;
  }
  .welcome h1 {
    font-family: Montserrat, sans-serif; font-weight: 300; font-size: 23px; line-height: 29.5px;
    color: var(--lilac); text-transform: uppercase;
  }
  .welcome p {
    margin-top: 20px; font-family: Montserrat, sans-serif; font-style: italic; font-weight: 600;
    font-size: 10px; color: var(--accent); text-transform: uppercase;
  }

  .section-bar {
    position: absolute; left: 133px; top: 555px; width: 930px; height: 19px;
    background: linear-gradient(#9a3ad6, #6c1ca0);
    font-family: Montserrat, sans-serif; font-weight: 600; font-size: 10px; color: var(--white);
    padding: 4px 0 0 16px;
  }
  .description {
    position: absolute; left: 137px; top: 593px; width: 612px;
    font-size: 11px; line-height: 14px; color: var(--text-muted);
  }
  .description p + p { margin-top: 14px; }

  .actions { position: absolute; left: 135px; top: 719px; display: flex; gap: 21px; }
  .action {
    width: 166px; height: 39px; border-radius: 7px; text-align: center;
    background: linear-gradient(#54306a, #3a1852 50%, #24092f);
    border: 1px solid #6b2a90; color: var(--white); padding-top: 2px;
  }
  .action strong { display: block; font-family: Montserrat, sans-serif; font-weight: 700; font-size: 14px; color: #d9cce6; }
  .action small { display: block; font-family: Montserrat, sans-serif; font-weight: 700; font-size: 7.5px; color: #d9cce6; text-transform: uppercase; }

  .glow-line {
    position: absolute; left: 133px; top: 805px; width: 680px; height: 2px;
    background: linear-gradient(90deg, rgba(180,90,230,0), #b46ae6 50%, #e8d0ff 88%, rgba(180,90,230,.2));
  }
  .feature-photo {
    position: absolute; left: 760px; top: 577px; width: 357px; height: 260px;
    background: radial-gradient(ellipse 140px 220px at 50% 55%, #e8dde8 0%, #a88a98 22%, #4a1a60 50%, rgba(12,2,16,0) 100%);
  }
</style>
</head>
<body>
<div class="page">
  <nav class="top-nav">
    <span>Home</span><span class="sep">|</span><span>About Us</span><span class="sep">|</span><span>Parties</span><span class="sep">|</span><span>Ladies Nights</span><span class="sep">|</span><span>Gallery</span><span class="sep">|</span><span>Mirelle's Blog</span><span class="sep">|</span><span>Advice</span><span class="sep">|</span><span>Business Opportunities</span><span class="sep">|</span><span>Reviews</span><span class="sep">|</span><span>Consultants</span><span class="sep">|</span><span>Toy Videos</span><span class="sep">|</span><span>Contact Us</span>
    <span class="account">Register Login</span>
  </nav>

  <header class="brand" role="img" aria-label="Sira Delcourt logo on a dark ornamental backdrop">
    <div class="brand-name">SIRA DELCOURT</div>
    <div class="brand-tagline">naughty things for nice girls, boys and you...</div>
  </header>

  <aside class="categories">
    <div class="categories-head">CATEGORIES</div>
    <ul>
      <li><span>ADULT TOYS</span></li>
      <li><span>LOTIONS &amp; POTIONS</span></li>
      <li class="active"><span>ACCESSORIES</span></li>
      <li><span>NOVELTIES</span></li>
      <li><span>BONDAGE</span></li>
    </ul>
    <div class="categories-foot"></div>
  </aside>

  <section class="welcome">
    <div class="welcome-inner">
      <h1>Welcome to Sira Delcourt<br>the sexiest sensuality boutiques<br>in South Africa.<br>If you are naughty but nice<br>looking for an adult store,<br>look no further than Sira<br>Delcourt.</h1>
      <p>Leading the adult industry since 2004.</p>
    </div>
  </section>

  <div class="section-bar">VELARA-XX WOMEN DESCRIPTION</div>
  <div class="description">
    <p>Lorem ipsum ea consul epicuri posidonium sed, oblique torquatos honestatis sea id. Vel ad dicam detraxit, assum ceteros corrumpit ei pro, vel ea congue quando officiis. No vix ceteros conceptam sententiae, vis ex audiam reformi-dans, cu aperiam evertitur interesset sed. Vis graeco minimum incorrupte no, qui eu quod perfecto senserit. Cibo aliq-uid electram et has, malorum molestiae pri et.</p>
    <p>Quo ne falli ubique. Laoreet assueverit mel ne, simul patrioque eam ad, mea cetero epicuri cu. Esse singulis postulant nam no. Id sonet theophrastus sit. sum quod complectitur eu. Ium iuvaret fabulas comprehensam ex.</p>
  </div>

  <div class="actions">
    <div class="action"><strong>JOIN US</strong><small>on Chatterly</small></div>
    <div class="action"><strong>FOLLOW US</strong><small>on Pipwave</small></div>
    <div class="action"><strong>BEST SELLERS</strong><small>all of the equipment!</small></div>
  </div>

  <div class="glow-line"></div>
  <div class="feature-photo" role="img" aria-label="Photo of a model in a white lace corset with glowing Sexiest Toys script lettering"></div>
</div>
</body>
</html>
```